Billboard design - consider what a billboard is

Design a billboard using my logo - Billboard is 6m x 3m
A Billboard is advertising for my company that is on a big sign.

Has to be clean and easy to read, and ideally highlights that we are Residential and Commercial builders.

Keep it clean and easy to read

The contact number for the board is

022 583 7092
www.harbourframeworks.co.nz
info@harbourframeworks.co.nz

Doesnt have to have all contact details if it doesnt fit

Has to catch peoples attention to contact us if they need a builder

Can you please change the sign to be all white writing, with black background ?
Updates

Please consider what a billboard is...

The design needs to be suitable for a billboard..

Target Market(s)

people driving past

Industry/Entity Type

Construction

Logo Text

Wellington Builder, website email address, contact number

Colors
0054AA
0677BA
7BADD7
CADEEF
E8F1F8

Requirements
Must have
• Easy to read
Nice to have
• easy to read, can clearly see contact details

```html
<!DOCTYPE html>
<html lang="en">
<head>
<meta charset="utf-8">
<title>Harbour Frameworks – Wellington Builder Billboard</title>
<link rel="stylesheet" href="https://fonts.googleapis.com/css2?family=Orbitron:wght@700&display=swap">
<style>
  :root {
    --page-bg: #ffffff;
    --board-bg: #000000;
    --board-edge: #2a2a2a;
    --brand-blue: #4a80c6;
    --text-white: #ffffff;
    --band-grey: #333333;
    --skyline-top: #3a3a3a;
    --skyline-base: #2e2e2e;
    --rule-grey: #3a3a3a;
  }
  html, body {
    margin: 0;
    width: 1200px;
    height: 1200px;
    overflow: hidden;
    background: var(--page-bg);
  }
  .billboard {
    display: block;
    width: 1200px;
    height: 1200px;
  }
  .board-face { fill: var(--board-bg); stroke: var(--board-edge); stroke-width: 1.5; }
  .brand-mark { fill: var(--brand-blue); }
  .brand-name { fill: var(--brand-blue); font-family: 'Orbitron', sans-serif; font-weight: 700; }
  .skyline-area { fill: url(#skylineTone); }
  .divider { stroke: var(--rule-grey); stroke-width: 1.5; }
  .headline { font-family: 'Orbitron', sans-serif; font-size: 46px; font-weight: 700; }
  .headline-place { fill: var(--text-white); }
  .headline-trade { fill: var(--brand-blue); }
  .phone-badge { fill: var(--brand-blue); }
  .phone-glyph { fill: #000000; }
  .phone-number { fill: var(--text-white); font-family: 'Orbitron', sans-serif; font-weight: 700; font-size: 44px; }
  .contact-band { fill: var(--band-grey); }
  .contact-line { fill: var(--text-white); font-family: 'Orbitron', sans-serif; font-weight: 700; font-size: 19px; }
</style>
</head>
<body>
<svg class="billboard" viewBox="0 0 1200 1200" xmlns="http://www.w3.org/2000/svg">
  <defs>
    <linearGradient id="skylineTone" x1="0" y1="0" x2="0" y2="1">
      <stop offset="0" stop-color="#3a3a3a"/>
      <stop offset="1" stop-color="#2e2e2e"/>
    </linearGradient>
  </defs>

  <rect class="board-face" x="266" y="422" width="671" height="358"/>

  <g class="brand-lockup">
    <rect class="brand-mark" x="304" y="505" width="38" height="38"/>
    <text class="brand-name" x="356" y="548" font-size="40" textLength="186" lengthAdjust="spacingAndGlyphs">HARBOUR</text>
    <text class="brand-name" x="356" y="576" font-size="15" textLength="186" lengthAdjust="spacingAndGlyphs">FRAMEWORKS</text>
  </g>

  <rect class="skyline-area" role="img" aria-label="City skyline silhouette with tall buildings and a needle tower"
        x="582" y="497" width="300" height="106"/>

  <line class="divider" x1="290" y1="603" x2="908" y2="603"/>

  <text class="headline" x="292" y="645" textLength="615" lengthAdjust="spacingAndGlyphs"><tspan class="headline-place">WELLINGTON</tspan> <tspan class="headline-trade">BUILDER</tspan></text>

  <line class="divider" x1="290" y1="650" x2="908" y2="650"/>

  <g class="phone-icon">
    <rect class="phone-badge" x="294" y="665" width="33" height="33" rx="7"/>
    <path class="phone-glyph" d="M301 672 l5 -1 l3 6 l-3 3 q3 6 8 9 l3 -3 l6 3 l-1 5 q-2 2 -5 1 q-11 -5 -16 -16 q-1 -4 0 -7 z"/>
  </g>
  <text class="phone-number" x="344" y="697" textLength="358" lengthAdjust="spacingAndGlyphs">022 583 7092</text>

  <polygon class="contact-band" points="267,708 791,708 757,762 267,762"/>
  <text class="contact-line" x="292" y="734" textLength="466" lengthAdjust="spacingAndGlyphs">www.harbourframeworks.co.nz</text>
  <text class="contact-line" x="292" y="755" textLength="444" lengthAdjust="spacingAndGlyphs">info@harbourframeworks.co.nz</text>
</svg>
</body>
</html>
```